Velvet Lantern Distillery

I need a label designed for my small distillery. I’d like it to have a rose, and the name velvet lantern in script writing. I need the graphic to fit a standard gin bottle and I’ll need to be able to edit it depending on alcohol, warning and descriptions. I want it to look elegant and attractive, but slightly daring too. It’s a 700ml oslo bottle
Target Market(s)
Bespoke gin and vodka drinkers
Industry/Entity Type
Beverage
Font styles to use
Script
Other font styles liked:
- Something easy to read
Requirements
Must have
- Room for me to add and remove text depending on the drink
Nice to have
- Velvet lantern in script, slight colour on the rose and black writing

```html
<!DOCTYPE html>
<html lang="en">
<head>
<meta charset="utf-8">
<title>Velvet Lantern – Gin Label</title>
<link rel="stylesheet" href="https://fonts.googleapis.com/css2?family=Pinyon+Script&family=Monsieur+La+Doulaise&family=Montserrat:wght@400;600&family=Oswald:wght@300;500&family=Crimson+Text:ital@1&display=swap">
<style>
  :root {
    --bg: #f4f5f7;
    --label: #f5f4ec;
    --strip: #fbfbf7;
    --ink: #1b1b1b;
    --rule: #3a3a3a;
    --gold: #c9a640;
    --rose-light: #f4c9cc;
    --rose-deep: #e58a98;
    --leaf: #6f9474;
  }
  * { margin: 0; padding: 0; box-sizing: border-box; }
  html, body { width: 1200px; height: 1182px; overflow: hidden; background: var(--bg); }
  .canvas { position: relative; width: 1200px; height: 1182px; }
  .label { position: absolute; background: var(--label); color: var(--ink); overflow: hidden; }

  /* Front label */
  .front { left: 60px; top: 276px; width: 556px; height: 630px; }
  .art { position: absolute; }
  .art-roses-top { left: 0; top: 0; width: 350px; height: 210px;
    background: radial-gradient(ellipse at 58% 40%, var(--rose-deep) 0%, var(--rose-light) 30%, rgba(244,201,204,0) 62%),
                radial-gradient(ellipse at 15% 35%, var(--leaf) 0%, rgba(111,148,116,0) 55%); }
  .art-leaves-left { left: 0; top: 190px; width: 110px; height: 200px;
    background: radial-gradient(ellipse at 30% 60%, var(--leaf) 0%, rgba(111,148,116,0) 70%); }
  .art-roses-bottom { left: 372px; top: 360px; width: 184px; height: 270px;
    background: radial-gradient(ellipse at 50% 18%, var(--rose-deep) 0%, var(--rose-light) 30%, rgba(244,201,204,0) 58%),
                radial-gradient(ellipse at 70% 70%, var(--leaf) 0%, rgba(111,148,116,0) 55%); }
  .brand { position: absolute; left: 0; width: 100%; font-family: "Pinyon Script", cursive; font-weight: 400; text-align: center; line-height: 1; }
  .brand-first { top: 172px; font-size: 84px; padding-left: 40px; }
  .brand-second { top: 262px; font-size: 108px; padding-left: 10px; }
  .brand-rule { position: absolute; left: 238px; top: 418px; width: 86px; height: 2px; background: var(--rule); }
  .small-batch { position: absolute; left: 160px; top: 456px; width: 240px; text-align: center;
    font-family: "Montserrat", sans-serif; font-weight: 600; font-size: 19px; letter-spacing: .38em; }
  .info-strip { position: absolute; left: 40px; top: 498px; width: 450px; height: 130px; background: var(--strip); overflow: hidden; }
  .seal { position: absolute; z-index: 2; left: 27px; top: 422px; width: 112px; height: 112px; border: 2px solid var(--gold); border-radius: 50%; }
  .seal::after { content: ""; position: absolute; inset: 26px; border: 1.5px solid var(--gold); border-radius: 50%; }
  .drink-name { position: absolute; left: 0; top: 14px; width: 100%; height: 40px; text-align: center;
    font-family: "Monsieur La Doulaise", cursive; font-size: 30px; line-height: 40px; }
  .strip-rule { position: absolute; left: 22px; width: 406px; height: 1px; background: var(--rule); }
  .strip-rule.upper { top: 58px; }
  .strip-rule.lower { top: 106px; }
  .specs { position: absolute; left: 22px; top: 64px; width: 406px; height: 38px; display: flex; align-items: flex-end;
    font-family: "Oswald", sans-serif; font-weight: 500; font-size: 22px; }
  .spec { flex: 1; text-align: center; }
  .spec-volume { font-size: 30px; border-left: 1px solid var(--rule); border-right: 1px solid var(--rule); line-height: 38px; }
  .spec-volume small { font-size: 20px; }
  .dots { flex: 0 0 44px; border-bottom: 1px dashed var(--rule); margin-bottom: 6px; }

  /* Back label */
  .back { left: 760px; top: 376px; width: 324px; height: 432px; }
  .back-roses { left: 222px; top: 0; width: 102px; height: 92px;
    background: radial-gradient(ellipse at 55% 35%, var(--rose-deep) 0%, var(--rose-light) 30%, rgba(244,201,204,0) 62%),
                radial-gradient(ellipse at 25% 80%, var(--leaf) 0%, rgba(111,148,116,0) 50%); }
  .back-brand { position: absolute; left: 20px; top: 18px; font-family: "Pinyon Script", cursive; font-weight: 400; font-size: 30px; }
  .back-rule { position: absolute; left: 128px; top: 82px; width: 56px; height: 1.5px; background: var(--rule); }
  .description { position: absolute; left: 16px; top: 98px; width: 292px; text-align: center;
    font-family: "Crimson Text", serif; font-style: italic; font-size: 12.5px; line-height: 1.3; }
  .warning { position: absolute; left: 16px; top: 204px; width: 292px; padding: 4px 8px; border: 1px solid var(--rule);
    font-family: "Montserrat", sans-serif; font-size: 9px; line-height: 1.32; }
  .ingredients { position: absolute; left: 16px; top: 306px; width: 296px; color: var(--ink);
    font-family: "Oswald", sans-serif; font-weight: 300; font-size: 9.5px; line-height: 1.4; }
  .ingredients strong { font-weight: 500; }
  .producer { position: absolute; left: 20px; top: 360px; font-family: "Montserrat", sans-serif; font-size: 10.5px; line-height: 1.3; }
</style>
</head>
<body>
<main class="canvas">
  <section class="label front">
    <div class="art art-roses-top" role="img" aria-label="Botanical illustration of pink roses with leaves"></div>
    <div class="art art-leaves-left" role="img" aria-label="Botanical illustration of rose leaves and stem"></div>
    <div class="art art-roses-bottom" role="img" aria-label="Botanical illustration of a pink rose spray"></div>
    <h1 class="brand brand-first">Velvet</h1>
    <div class="brand brand-second">Lantern</div>
    <div class="brand-rule"></div>
    <p class="small-batch">SMALL BATCH</p>
    <div class="info-strip">
      <p class="drink-name">My Drink Name</p>
      <div class="strip-rule upper"></div>
      <div class="specs">
        <span class="dots"></span>
        <span class="spec">% ALC/VOL</span>
        <span class="spec spec-volume">700<small>ML</small></span>
        <span class="spec">BATCH NO</span>
        <span class="dots"></span>
      </div>
      <div class="strip-rule lower"></div>
    </div>
    <div class="seal" aria-hidden="true"></div>
  </section>

  <section class="label back">
    <div class="art back-roses" role="img" aria-label="Small botanical illustration of pink roses"></div>
    <h2 class="back-brand">Velvet Lantern</h2>
    <div class="back-rule"></div>
    <p class="description">Lorem ipsum dolor sit amet, consectetuer adipiscing elit, sed diam nonummy nibh euismod tincidunt ut laoreet dolore magna aliquam erat volutpat. Ut wisi enim ad minim veniam, quis nostrud exerci tation ullamcorper suscipit lobortis nisl ut aliquip ex ea commodo consequat.</p>
    <p class="warning">GOVERNMENT WARNING: Lorem ipsum dolor sit amet, consectetuer adipiscing elit, sed diam nonummy nibh euismod tincidunt ut laoreet dolore magna aliquam erat volutpat. Ut wisi enim ad minim veniam, quis nostrud exerci tation ullamcorper suscipit lobortis nisl ut aliquip ex ea commodo consequat. dolore te feugait nulla facilisi.</p>
    <p class="ingredients" spellcheck="false"><strong>INGREDIENTS</strong>: Lorem ipsum dolor sit amet, consectetuer adipiscing elit, sed diam nonummy nibh euismod tincidunt ut laoreet dolore magna aliquam erat volutpat.</p>
    <p class="producer">PRODUCER<br>Company<br>Address<br>Phone<br>www.velvetlantern.co</p>
  </section>
</main>
</body>
</html>
```